Wealth Education Business Needs Sharp Business Card Design

We need a business card design for a recently launched investor education business called Harbor Crest.

The final design should promote security, empowerment, self improvement and financial gain. The card will ideally promote the stature of the business.

For more information and colours please visit harborcrest.com.au

Target Market(s)

Corporate executives and high net worth individuals

Industry/Entity Type

Education

Contact Information for Business Card

Name
Position
Contact Address
Phone
Mobile
Email
Website

```html
<!DOCTYPE html>
<html lang="en">
<head>
<meta charset="utf-8">
<title>Harbor Crest — Business Card</title>
<link href="https://fonts.googleapis.com/css2?family=Jost:wght@400;500&display=swap" rel="stylesheet">
<style>
  :root {
    --backdrop: #dadada;
    --card: #ffffff;
    --navy: #1e2a3c;
    --ink: #232b38;
    --muted: #9a9ea5;
    --accent: #1fa2b8;
    --on-navy: #eef1f5;
  }
  html, body {
    margin: 0;
    width: 1200px;
    height: 1200px;
    overflow: hidden;
    background: var(--backdrop);
    font-family: "Jost", "Futura", sans-serif;
  }
  .card {
    position: absolute;
    width: 620px;
    height: 387px;
    background: var(--card);
    overflow: hidden;
  }
  .card--front { left: 231px; top: 204px; }
  .card--back  { left: 392px; top: 657px; }

  .brand {
    position: absolute;
    display: flex;
    align-items: center;
    gap: 12px;
  }
  .brand__mark {
    width: 22px;
    height: 22px;
    background: var(--accent);
  }
  .brand__name {
    font-weight: 500;
    text-transform: uppercase;
    letter-spacing: 0.14em;
    line-height: 1;
  }

  .card--front .brand { left: 343px; top: 62px; }
  .card--front .brand__name { font-size: 25px; color: var(--ink); }

  .office {
    position: absolute;
    left: 343px;
    top: 96px;
    margin: 0;
    font-size: 12.5px;
    line-height: 18px;
    font-weight: 500;
    color: var(--ink);
    font-style: normal;
  }

  .person {
    position: absolute;
    left: 31px;
    top: 199px;
  }
  .person__name {
    margin: 0;
    font-size: 21px;
    font-weight: 400;
    color: var(--ink);
    line-height: 30px;
  }
  .person__role {
    margin: 0;
    font-size: 12px;
    color: var(--muted);
    line-height: 20px;
  }
  .divider {
    position: absolute;
    left: 164px;
    right: 0;
    top: 216px;
    height: 2px;
    background: var(--ink);
  }

  .contact-band {
    position: absolute;
    left: 0;
    right: 0;
    bottom: 0;
    height: 99px;
    background: var(--navy);
    color: var(--on-navy);
    font-size: 15px;
    line-height: 22px;
  }
  .contact-band__col {
    position: absolute;
    top: 31px;
    margin: 0;
    font-style: normal;
  }
  .contact-band__col--phones { left: 36px; }
  .contact-band__col--online { left: 343px; }

  .identity-band {
    position: absolute;
    left: 0;
    top: 147px;
    width: 417px;
    height: 96px;
    background: var(--navy);
  }
  .card--back .brand { left: 62px; top: 36px; }
  .card--back .brand__name { font-size: 27px; color: var(--on-navy); }
  .foot-band {
    position: absolute;
    left: 0;
    right: 0;
    bottom: 0;
    height: 16px;
    background: var(--navy);
  }
</style>
</head>
<body>

<section class="card card--front">
  <div class="brand">
    <span class="brand__name">Harbor Crest</span>
  </div>
  <address class="office">
    Office:<br>
    Level 2, 214 Tidewater Lane,<br>
    Southbank VIC 3006
  </address>

  <div class="person">
    <p class="person__name">Your Name</p>
    <p class="person__role">Senior Trading Strategist</p>
  </div>
  <div class="divider"></div>

  <div class="contact-band">
    <p class="contact-band__col contact-band__col--phones">
      tel: 1300 555 014<br>
      fax: 1300 555 016
    </p>
    <address class="contact-band__col contact-band__col--online">
      mail: support@harborcrest.com.au<br>
      web: www.harborcrest.com.au
    </address>
  </div>
</section>

<section class="card card--back">
  <div class="identity-band">
    <div class="brand">
      <span class="brand__mark"></span>
      <span class="brand__name">Harbor Crest</span>
    </div>
  </div>
  <div class="foot-band"></div>
</section>

</body>
</html>
```